Need a flyer overhaul and minor changes

flyer is 5.5" x 8.5" we need to change the $250.00 to $325.00, update our company logo on the brochure, and also have an area where we can have the store address (318 W Harlan Ave, Del Rio, TX 78840 - (830) 642-9158). I've attached a our current brochure and our updated logo and we just want to make look better and updated.

Industry/Entity Type

Lending and Finance

Requirements
Nice to have
• updated layout and pictures

```html
<!DOCTYPE html>
<html lang="en">
<head>
<meta charset="utf-8">
<title>Ridgeline Lending – Title Loan Comparison Flyer</title>
<link href="https://fonts.googleapis.com/css2?family=Barlow+Condensed:wght@300;400;700&family=Montserrat:wght@300;500;600;700;800&display=swap" rel="stylesheet">
<style>
  :root {
    --brand-red: #c1272d;
    --brand-green: #225435;
    --row-green: #3f8c5c;
    --paper: #ffffff;
    --backdrop: #e6e6e6;
    --photo-light: #efe9e4;
    --photo-mid: #cfc2b6;
  }
  * { margin: 0; padding: 0; box-sizing: border-box; }
  html, body { width: 857px; height: 1200px; overflow: hidden; }
  body { background: var(--backdrop); position: relative; font-family: 'Montserrat', sans-serif; }

  .flyer {
    position: absolute; left: 56px; top: 25px;
    width: 744px; height: 1150px;
    background: var(--paper); overflow: hidden;
    box-shadow: 0 6px 24px rgba(0,0,0,0.25);
  }
  .flyer > * { position: absolute; }

  .top-band { left: 0; top: 0; width: 744px; height: 184px; background: var(--brand-red); }
  .headline {
    left: 0; top: 58px; width: 744px; text-align: center; white-space: nowrap;
    font-family: 'Barlow Condensed', sans-serif; font-weight: 400;
    font-size: 70px; line-height: 1; color: var(--paper);
    text-shadow: 2px 3px 0 rgba(90,10,10,0.45);
  }
  .headline strong { font-weight: 700; }

  .comparison-title {
    left: 64px; top: 150px; width: 616px; height: 70px;
    background: var(--brand-green); border-radius: 6px;
    color: var(--paper); font-weight: 800; font-size: 38px; white-space: nowrap;
    display: flex; align-items: center; justify-content: center;
  }

  .hero-photo {
    left: 0; top: 271px; width: 357px; height: 620px;
    background: radial-gradient(ellipse at 50% 35%, var(--photo-light), var(--photo-mid));
  }

  .col-head-brand {
    left: 353px; top: 296px; width: 124px; text-align: center;
    font-weight: 700; font-size: 17px; line-height: 1.1; color: var(--brand-green);
  }
  .col-head-title {
    left: 500px; top: 290px; width: 180px; text-align: right; white-space: nowrap;
    font-family: 'Barlow Condensed', sans-serif; font-weight: 700;
    font-size: 44px; line-height: 1; letter-spacing: -0.5px; color: var(--brand-green);
  }
  .table-rule { left: 353px; width: 327px; height: 2px; background: var(--brand-green); }
  .rule-top { top: 343px; }
  .rule-bottom { top: 779px; }
  .table-divider { left: 515px; top: 344px; width: 2px; height: 436px; background: var(--brand-green); }

  .payment-list { list-style: none; top: 364px; font-weight: 600; font-size: 21px; white-space: nowrap; }
  .payment-list li { height: 32.8px; line-height: 32.8px; display: flex; }
  .payment-list .month { width: 36px; text-align: center; color: var(--row-green); font-weight: 500; }
  .list-ours { left: 351px; }
  .list-ours .amount { margin-left: 17px; color: var(--brand-red); }
  .list-title { left: 540px; }
  .list-title .amount { margin-left: 17px; color: var(--brand-green); }

  .result-paid {
    left: 353px; top: 806px; font-weight: 800; font-size: 27px; white-space: nowrap;
    line-height: 1; color: var(--brand-green);
  }
  .result-owe {
    left: 526px; top: 808px; width: 154px; text-align: right; white-space: nowrap;
    font-weight: 800; font-size: 25px; line-height: 1; color: var(--brand-red);
  }
  .owe-amount {
    left: 526px; top: 834px; width: 154px; height: 49px;
    background: var(--brand-red); color: var(--paper);
    font-weight: 700; font-size: 40px;
    display: flex; align-items: center; justify-content: center;
  }

  .footer-shapes { left: 0; top: 880px; width: 744px; height: 100px; }

  .footer-brand {
    left: 42px; top: 1000px; width: 250px; white-space: nowrap;
    display: flex; align-items: center; gap: 10px;
    font-weight: 700; font-size: 21px; color: var(--brand-green);
  }
  .footer-brand .mark { width: 14px; height: 14px; background: var(--brand-red); flex: none; }

  .phone-box {
    left: 337px; top: 953px; width: 343px; height: 56px;
    background: var(--brand-green); border-radius: 5px; white-space: nowrap;
    display: flex; align-items: center; justify-content: center;
    color: var(--paper); font-weight: 700; font-size: 35px;
  }
  .store-address {
    left: 337px; top: 1023px; width: 343px; text-align: right; white-space: nowrap;
    font-weight: 700; font-size: 17.5px; color: var(--brand-red);
  }

  .bottom-band {
    left: 0; top: 1075px; width: 744px; height: 75px; background: var(--brand-red);
    display: flex; align-items: center; justify-content: center; white-space: nowrap;
    color: var(--paper); font-size: 22px;
  }
  .bottom-band .visit { font-weight: 300; letter-spacing: 0.32em; margin-right: 10px; }
  .bottom-band .site { font-weight: 800; letter-spacing: 0.14em; }
</style>
</head>
<body>
  <main class="flyer">
    <div class="top-band"></div>
    <h1 class="headline">STUCK IN A <strong>TITLE LOAN?</strong></h1>
    <h2 class="comparison-title">$1,000 LOAN COMPARISON</h2>

    <div class="hero-photo" role="img" aria-label="Photo of a smiling woman in a white t-shirt and jeans holding a fan of dollar bills"></div>

    <div class="col-head-brand">Ridgeline Lending</div>
    <div class="col-head-title">TITLE LOAN</div>
    <div class="table-rule rule-top"></div>
    <div class="table-divider"></div>
    <div class="table-rule rule-bottom"></div>

    <ol class="payment-list list-ours">
      <li><span class="month">1</span><span class="amount">$131.67</span></li>
      <li><span class="month">2</span><span class="amount">$131.67</span></li>
      <li><span class="month">3</span><span class="amount">$131.67</span></li>
      <li><span class="month">4</span><span class="amount">$131.67</span></li>
      <li><span class="month">5</span><span class="amount">$131.67</span></li>
      <li><span class="month">6</span><span class="amount">$131.67</span></li>
      <li><span class="month">7</span><span class="amount">$131.67</span></li>
      <li><span class="month">8</span><span class="amount">$131.67</span></li>
      <li><span class="month">9</span><span class="amount">$131.67</span></li>
      <li><span class="month">10</span><span class="amount">$131.67</span></li>
      <li><span class="month">11</span><span class="amount">$131.67</span></li>
      <li><span class="month">12</span><span class="amount">$131.67</span></li>
    </ol>
    <ol class="payment-list list-title">
      <li><span class="month">1</span><span class="amount">$325.00</span></li>
      <li><span class="month">2</span><span class="amount">$325.00</span></li>
      <li><span class="month">3</span><span class="amount">$325.00</span></li>
      <li><span class="month">4</span><span class="amount">$325.00</span></li>
      <li><span class="month">5</span><span class="amount">$325.00</span></li>
      <li><span class="month">6</span><span class="amount">$325.00</span></li>
      <li><span class="month">7</span><span class="amount">$325.00</span></li>
      <li><span class="month">8</span><span class="amount">$325.00</span></li>
      <li><span class="month">9</span><span class="amount">$325.00</span></li>
      <li><span class="month">10</span><span class="amount">$325.00</span></li>
      <li><span class="month">11</span><span class="amount">$325.00</span></li>
      <li><span class="month">12</span><span class="amount">$325.00</span></li>
    </ol>

    <div class="result-paid">PAID OFF</div>
    <div class="result-owe">STILL OWE</div>
    <div class="owe-amount">$1,000</div>

    <svg class="footer-shapes" viewBox="0 0 744 100" aria-hidden="true">
      <polygon points="0,9 259,9 262,14 0,14" fill="var(--brand-red)"/>
      <polygon points="289,41 744,41 744,86 319,86" fill="var(--brand-red)"/>
      <line x1="262" y1="13" x2="310" y2="84" stroke="var(--brand-green)" stroke-width="7"/>
    </svg>

    <div class="footer-brand"><span class="mark"></span>Ridgeline Lending</div>

    <div class="phone-box">(830) 642-9158</div>
    <div class="store-address">318 W Harlan Ave, Del Rio, TX 78840</div>

    <div class="bottom-band"><span class="visit">VISIT US AT</span><span class="site">RIDGELINELENDING.COM</span></div>
  </main>
</body>
</html>
```